Signage. Will be for store front. Building is on a corner lot. Lots of traffic.

Opening a new location for our landscape business with a garden store (boutique theme) which will have big pottery pots, house plants, ferns and orchids for sale.

And on the side lot of the store we will have bigger bulk items(contractors theme) landscape plants, sod, mulch, soil, rock for sale.

Sign is about 8’x6’

Target Market(s)

Home owners
Landscapers
Builders

Industry/Entity Type

Landscaping

Font styles to use
Sans Serif

Colors
9bcb3c

Requirements
Must have
• “ Installation and Delivery” is a big deal to let people know we do that
Nice to have
• Added a first rendition idea but don’t love it
Added a file with some words to play with
Need help with the words
Should not have
• ?

```html
<!DOCTYPE html>
<html lang="en">
<head>
<meta charset="utf-8">
<title>Fernbrook Gardens – Storefront Sign</title>
<link rel="stylesheet" href="https://fonts.googleapis.com/css2?family=Anton&family=Poppins:wght@700;800&display=swap">
<style>
  :root {
    --backdrop: #7a7a7a;
    --sign-white: #ffffff;
    --olive: #556227;
    --olive-light: #9bcb3c;
    --brand-green: #6f8f2e;
    --ink: #222820;
    --footer: #232a1f;
    --tick: #5a6b2a;
  }
  * { margin: 0; padding: 0; box-sizing: border-box; }
  html, body { width: 1200px; height: 1000px; overflow: hidden; }
  body {
    background: var(--backdrop);
    position: relative;
    font-family: "Poppins", sans-serif;
  }
  .sign {
    position: absolute;
    left: 112px; top: 96px;
    width: 977px; height: 732px;
    background: var(--sign-white);
  }
  .brand {
    position: absolute;
    left: 0; right: 0; top: 0; height: 182px;
    display: flex; align-items: center; justify-content: center; gap: 22px;
  }
  .brand-name {
    font-family: "Poppins", sans-serif;
    font-weight: 700;
    font-size: 56px;
    color: var(--brand-green);
    letter-spacing: 1px;
  }
  .brand-dot {
    width: 64px; height: 64px; border-radius: 50%;
    background: var(--olive-light);
  }
  .welcome-band {
    position: absolute;
    left: 0; right: 0; top: 186px; height: 180px;
    background:
      linear-gradient(90deg, transparent, var(--olive-light) 50%, transparent) top / 100% 8px no-repeat,
      linear-gradient(90deg, transparent, var(--olive-light) 50%, transparent) bottom / 100% 8px no-repeat;
    padding: 8px 0;
  }
  .welcome-band-inner {
    height: 100%;
    background: var(--olive);
    display: flex; align-items: center; justify-content: center;
  }
  .welcome-title {
    font-family: "Anton", sans-serif;
    font-size: 134px;
    line-height: 1;
    color: var(--sign-white);
    letter-spacing: 3px;
    text-shadow: 4px 4px 0 #1e2410;
    margin-top: 6px;
  }
  .services {
    position: absolute;
    top: 398px;
    list-style: none;
  }
  .services-left { left: 62px; }
  .services-right { left: 498px; top: 402px; }
  .services li {
    display: flex; align-items: center; gap: 14px;
    font-weight: 700;
    font-size: 29px;
    color: var(--ink);
    letter-spacing: 0.3px;
    line-height: 1;
  }
  .services-left li { height: 53px; }
  .services-right li { height: 40px; gap: 12px; }
  .tick { width: 36px; height: 36px; flex: none; }
  .footer-band {
    position: absolute;
    left: 0; right: 0; bottom: 0; height: 106px;
    background: var(--footer);
    display: flex; align-items: center; justify-content: center;
  }
  .footer-text {
    font-weight: 800;
    font-size: 38px;
    color: #f1f1ee;
    letter-spacing: 0.5px;
  }
</style>
</head>
<body>
  <svg width="0" height="0" style="position:absolute">
    <symbol id="tick-icon" viewBox="0 0 36 36">
      <circle cx="16" cy="19" r="13.5" fill="none" stroke="var(--tick)" stroke-width="2.5"/>
      <path d="M9 18 L15 25 L31 5" fill="none" stroke="var(--tick)" stroke-width="4.5" stroke-linecap="round" stroke-linejoin="round"/>
    </symbol>
  </svg>

  <main class="sign">
    <header class="brand">
      <span class="brand-name">Fernbrook Gardens</span>
      <span class="brand-dot"></span>
    </header>

    <section class="welcome-band">
      <div class="welcome-band-inner">
        <h1 class="welcome-title">PUBLIC WELCOME !</h1>
      </div>
    </section>

    <ul class="services services-left">
      <li><svg class="tick"><use href="#tick-icon"/></svg>GARDEN CENTER</li>
      <li><svg class="tick"><use href="#tick-icon"/></svg>LANDSCAPE SUPPLY</li>
      <li><svg class="tick"><use href="#tick-icon"/></svg>GARDEN SHOP</li>
      <li><svg class="tick"><use href="#tick-icon"/></svg>GARDEN SUPPLY</li>
    </ul>

    <ul class="services services-right">
      <li><svg class="tick"><use href="#tick-icon"/></svg>SOD</li>
      <li><svg class="tick"><use href="#tick-icon"/></svg>NURSERY</li>
      <li><svg class="tick"><use href="#tick-icon"/></svg>LANDSCAPING</li>
      <li><svg class="tick"><use href="#tick-icon"/></svg>LAWN &amp; GARDEN</li>
      <li><svg class="tick"><use href="#tick-icon"/></svg>NURSERY &amp; GARDEN</li>
    </ul>

    <footer class="footer-band">
      <p class="footer-text">INSTALLATION &amp; DELIVERY AVAILABLE</p>
    </footer>
  </main>
</body>
</html>
```